Corporate Profile, with ALOT more work for winning bidder

We need
1. CD designed
2. CD Cover Designed
3. 2x Envelope's designed
4. Letter head designed
The designer picked will also get many further projects from us. Almost totaling 10k a year.
- More info
• Software installation disc
a. Logo
b. Contact details (See below)
c. Instructions
o “Please insert CD into computer and follow the prompts”
d. Title
o “Free Software Installation Disc”
• CD Sleave double sided
- Front
o Logo
o Website Address
o Facebook address
o Title
? “Free Software Installation Disc”
• Letter head
- Logo
- Contact information
- A4 paper size
• C4 Envelope
- Nicely Designed with logo
- A window to put address
- Printed return address (See below) on back
• DL Envelope, to return to us
- Had our return address ( See below)
- Nice design
Contact details
Machines Near You
7b Fenwick Crescent Bayswater, Vic, 3153
www.MachinesNearYou.example.au
1300 42 65 19
www.Facebook.com/MachinesNearYou
Return Address
Machines Near You
7b Fenwick Crescent
Kestrel Park, Vic, 3999

```html
<!DOCTYPE html>
<html lang="en">
<head>
<meta charset="utf-8">
<title>Machines Near You – C4 Envelope Back</title>
<link rel="stylesheet" href="https://fonts.googleapis.com/css2?family=Arimo:wght@700&family=Source+Sans+3:wght@400;600;700&display=swap">
<style>
  :root {
    --page: #ffffff;
    --envelope-light: #707073;
    --envelope-dark: #58585a;
    --brand-blue: #00aee0;
    --brand-orange: #f39a1e;
    --address-white: #ffffff;
    --caption-grey: #a9a9ab;
    --mark-blue: #5cc6ef;
  }
  html, body {
    margin: 0;
    padding: 0;
    overflow: hidden;
    background: var(--page);
  }
  .canvas {
    position: relative;
    width: 1200px;
    height: 849px;
    overflow: hidden;
    background: var(--page);
  }
  .envelope {
    position: absolute;
    left: 136px;
    top: 99px;
    width: 927px;
    height: 654px;
    background: var(--envelope-light);
    overflow: hidden;
  }
  .envelope-flap {
    position: absolute;
    inset: 0;
  }
  .return-address {
    position: absolute;
    left: 119px;
    top: 259px;
    margin: 0;
    font-style: normal;
  }
  .return-address__name {
    display: block;
    font-family: "Source Sans 3", sans-serif;
    font-weight: 600;
    font-size: 20px;
    letter-spacing: 3.9px;
    color: var(--brand-blue);
    line-height: 27px;
  }
  .return-address__name .accent {
    color: var(--brand-orange);
    font-weight: 400;
  }
  .return-address__line {
    display: block;
    font-family: "Arimo", sans-serif;
    font-weight: 700;
    font-size: 17.5px;
    letter-spacing: 0.2px;
    color: var(--address-white);
    line-height: 26px;
  }
  .brand-signoff {
    position: absolute;
    left: 595px;
    top: 466px;
    width: 300px;
    text-align: center;
  }
  .brand-signoff__dot {
    display: block;
    width: 108px;
    height: 108px;
    margin: 0 auto 6px;
    border-radius: 50%;
    background: var(--mark-blue);
  }
  .brand-signoff__name {
    display: block;
    font-family: "Source Sans 3", sans-serif;
    font-weight: 700;
    font-size: 30px;
    line-height: 36px;
    color: var(--brand-blue);
    white-space: nowrap;
  }
  .caption {
    position: absolute;
    left: 136px;
    top: 762px;
    margin: 0;
    font-family: "Source Sans 3", sans-serif;
    font-weight: 400;
    font-size: 20px;
    color: var(--caption-grey);
  }
</style>
</head>
<body>
<main class="canvas">
  <section class="envelope" aria-label="C4 envelope, back">
    <svg class="envelope-flap" width="927" height="654" viewBox="0 0 927 654" aria-hidden="true">
      <defs>
        <filter id="flap-shadow" x="-10%" y="-10%" width="130%" height="130%">
          <feDropShadow dx="3" dy="4" stdDeviation="4" flood-color="#000" flood-opacity="0.55"/>
        </filter>
      </defs>
      <path d="M0 0 H742 C765 260 620 630 0 654 Z" fill="var(--envelope-dark)" filter="url(#flap-shadow)"/>
    </svg>

    <address class="return-address">
      <span class="return-address__name">MACHINES <span class="accent">NEAR</span> YOU</span>
      <span class="return-address__line">7b Fenwick Crescent</span>
      <span class="return-address__line">Kestrel Park, Vic, 3999</span>
    </address>

    <div class="brand-signoff">
      <span class="brand-signoff__dot" aria-hidden="true"></span>
      <span class="brand-signoff__name">MACHINES NEAR YOU</span>
    </div>
  </section>

  <p class="caption">C4 Envelope Back</p>
</main>
</body>
</html>
```